Relationship Seminar

I am an Author and Speaker and I need a flyer for a Christian relationship seminar targeting women aged between mid 20's to late 30's. It's an event for women only.

-I am looking for a fresh/ edgy look but still feminine
-Nothing too girly
-Maximum of 3 colours (Spring colours are good)
-I want the flyer to convey joy or happiness
-Use my photo which is attached as the predominant image (you can crop it to remove the background etc)

The Flyer Details are as follows:

Somewhere Past Tomorrow - Brisbane Tour

Join Author & Speaker, Rosalind Okafe, as she speaks about her new book entitled 'Somewhere Past Tomorrow'.

Be inspired and encouraged to embrace the life that God has given you and make the most of it!

Date: Saturday 9th November 2013
Time: 2:00 pm - 5:00 pm
Location: Larkwell Hotel Brisbane (Juniper Ballroom)
Fennimore Street, Brisbane QLD 4000
Tickets: $60/pp (Includes High Tea)
Buy Tickets: www.rosalindokafe.com or http://somewherepasttomorrow.ticketvane.net

Email: info@rosalindokafe.com

Include the cover of my new book.

www.rosalindokafe.com (include my website at the bottom of the flyer)

Target Market(s)

Young professional women aged between their mid 20's to late 30's

Industry/Entity Type

Event

Requirements
Should not have
• -No girly or curly font

```html
<!DOCTYPE html>
<html lang="en">
<head>
<meta charset="utf-8">
<title>Somewhere Past Tomorrow – Brisbane Tour Flyer</title>
<link rel="stylesheet" href="https://fonts.googleapis.com/css2?family=Cinzel:wght@400;700&family=Questrial&family=Arimo:ital,wght@0,400;0,700;1,400;1,700&family=Tinos:ital,wght@1,700&display=swap">
<style>
  :root {
    --backdrop: #e9e6e2;
    --wood-light: #c9ab84;
    --wood-mid: #b08e66;
    --cover-white: #fbfbfb;
    --cover-red: #d9452b;
    --cover-grey: #6b6b6b;
    --cover-band: #e3ecd9;
    --cover-green: #8cc47a;
    --tour-yellow: #f2e21c;
    --title-white: #ffffff;
    --purple: #662d91;
    --green: #39b54a;
    --light-grey: #ebebeb;
    --price-red: #ec2f2f;
    --link-orange: #f5a31a;
    --ink: #222222;
  }
  * { box-sizing: border-box; margin: 0; padding: 0; }
  html, body { width: 1200px; height: 1000px; overflow: hidden; }
  body {
    background: var(--backdrop);
    font-family: "Questrial", "Century Gothic", sans-serif;
    position: relative;
  }
  .flyer {
    position: absolute;
    top: 105px;
    width: 555px;
    height: 790px;
    overflow: hidden;
    box-shadow: 0 4px 14px rgba(0,0,0,.18);
  }
  .flyer--front { left: 30px; }
  .flyer--back { left: 615px; background: #fff; }

  /* Front */
  .wood-set {
    position: absolute; inset: 0;
    background: linear-gradient(180deg, var(--wood-light) 0%, var(--wood-mid) 55%, var(--wood-light) 62%, var(--wood-mid) 100%);
  }
  .book-cover {
    position: absolute;
    background: var(--cover-white);
    box-shadow: 3px 4px 10px rgba(0,0,0,.3);
    text-align: center;
    display: flex; flex-direction: column;
  }
  .book-cover--front { left: 170px; top: 128px; width: 245px; height: 458px; }
  .book-cover__title {
    font-family: "Cinzel", serif;
    color: var(--cover-red);
    line-height: 1.05;
  }
  .book-cover--front .book-cover__title { font-size: 27px; padding-top: 24px; }
  .book-cover__subtitle {
    color: var(--cover-grey);
    font-family: "Arimo", sans-serif;
    line-height: 1.3;
    margin-top: 8px;
  }
  .book-cover--front .book-cover__subtitle { font-size: 13px; }
  .book-cover__photo {
    flex: 1;
    margin-top: 10px;
    background: linear-gradient(180deg, #f4f4f4, #d8d8d8 60%, #e8e8e8);
  }
  .book-cover__author {
    background: var(--cover-band);
    color: var(--cover-grey);
    font-family: "Arimo", sans-serif;
    border-bottom: 6px solid var(--cover-green);
  }
  .book-cover--front .book-cover__author { font-size: 13px; padding: 7px 0; }

  .tour {
    position: absolute; left: 0; right: 0; top: 592px;
    text-align: center;
  }
  .tour__label {
    font-family: "Tinos", serif;
    font-weight: 700; font-style: italic;
    color: var(--tour-yellow);
    font-size: 21px;
    margin-left: -60px;
  }
  .tour__title {
    font-family: "Cinzel", serif;
    font-weight: 400;
    color: var(--title-white);
    font-size: 46px;
    line-height: 1.05;
    text-shadow: 2px 3px 4px rgba(0,0,0,.35);
    margin-top: 4px;
  }
  .tour__title span { display: block; }

  /* Back */
  .author-photo {
    position: absolute; left: 0; top: 0; width: 100%; height: 325px;
    background: linear-gradient(90deg, #c98f7a 0%, #ead8d0 45%, #4a3a34 70%, #d8cfcc 100%);
  }
  .book-cover--back { left: 72px; top: 92px; width: 128px; height: 233px; z-index: 2; }
  .book-cover--back .book-cover__title { font-size: 15px; padding-top: 10px; }
  .book-cover--back .book-cover__subtitle { font-size: 8px; margin-top: 4px; }
  .book-cover--back .book-cover__photo { margin-top: 6px; }
  .book-cover--back .book-cover__author { font-size: 8px; padding: 3px 0; border-bottom-width: 4px; }

  .band { position: absolute; left: 0; width: 100%; padding: 0 30px 0 40px; }
  .band--intro {
    top: 325px; height: 122px;
    background: var(--purple); color: #fff;
    font-size: 16.5px; line-height: 1.3;
    display: flex; align-items: center;
  }
  .band--details {
    top: 447px; height: 123px;
    background: var(--green); color: #fff;
    font-size: 17px; line-height: 1.3;
    display: flex; flex-direction: column; justify-content: center;
  }
  .band--details em { font-family: "Arimo", sans-serif; font-weight: 700; }
  .band--tickets {
    top: 570px; height: 100px;
    background: var(--light-grey);
    display: flex; align-items: center;
  }
  .tickets__label { font-family: "Arimo", sans-serif; font-style: italic; font-size: 24px; color: var(--ink); width: 85px; }
  .tickets__price { text-align: center; }
  .tickets__amount {
    font-family: "Arimo", sans-serif; font-weight: 700; font-style: italic;
    color: var(--price-red); font-size: 50px; line-height: 1;
  }
  .tickets__note { font-family: "Arimo", sans-serif; font-style: italic; font-size: 21px; color: var(--ink); }
  .band--contact {
    top: 670px; height: 120px;
    font-family: "Arimo", sans-serif;
    display: flex; flex-direction: column; justify-content: center;
    font-size: 14.5px; line-height: 1.35;
  }
  .contact__link { color: var(--link-orange); }
  .contact__link a { color: var(--link-orange); text-decoration: underline; }
  .contact__web { font-weight: 700; color: var(--ink); margin-top: 14px; font-size: 14.5px; }
</style>
</head>
<body>

<section class="flyer flyer--front">
  <div class="wood-set" role="img" aria-label="Photographed wooden panel wall and floor backdrop"></div>
  <div class="book-cover book-cover--front">
    <div class="book-cover__title">Somewhere<br>Past Tomorrow</div>
    <div class="book-cover__subtitle">A Walk from<br>Waiting towards Promise</div>
    <div class="book-cover__photo" role="img" aria-label="Cover photo of a young woman in a white dress between two young men"></div>
    <div class="book-cover__author">Rosalind Okafe</div>
  </div>
  <div class="tour">
    <div class="tour__label">Brisbane Tour</div>
    <h1 class="tour__title"><span>Somewhere</span><span>Past Tomorrow</span></h1>
  </div>
</section>

<section class="flyer flyer--back">
  <div class="author-photo" role="img" aria-label="Photo of the smiling author in a leather jacket against a brick wall"></div>
  <div class="book-cover book-cover--back">
    <div class="book-cover__title">Somewhere<br>Past Tomorrow</div>
    <div class="book-cover__subtitle">A Walk from<br>Waiting towards Promise</div>
    <div class="book-cover__photo" role="img" aria-label="Cover photo of a young woman in a white dress between two young men"></div>
    <div class="book-cover__author">Rosalind Okafe</div>
  </div>

  <div class="band band--intro">
    <p>Join Author &amp; Speaker, Rosalind Okafe, as she speaks about her new book entitled 'Somewhere Past Tomorrow'. Be inspired and encouraged to embrace the life that God has given you and make the most of it!</p>
  </div>

  <div class="band band--details">
    <p>Saturday 9th November 2013</p>
    <p>2:00 pm - 5:00 pm</p>
    <p>Larkwell Hotel Brisbane <em>(Juniper Ballroom)</em></p>
    <p>Fennimore Street, Brisbane QLD 4000</p>
  </div>

  <div class="band band--tickets">
    <span class="tickets__label">Tickets:</span>
    <div class="tickets__price">
      <div class="tickets__amount">$60/pp</div>
      <div class="tickets__note">(Includes High Tea)</div>
    </div>
  </div>

  <div class="band band--contact">
    <p class="contact__link">Buy <a>Tickets:www.rosalindokafe.com</a></p>
    <p class="contact__link">or <a>http://somewherepasttomorrow.ticketvane.net</a></p>
    <p class="contact__web">info@rosalindokafe.com &nbsp;/&nbsp; www.rosalindokafe.com</p>
  </div>
</section>

</body>
</html>
```